Building certification business in Sydney Australia

Brookvale Assessors is a small business that is currently growing and needs a profession looking website to attract customers and give them all the information they need. The main services we offer currently are pre-purchase building inspections for purchasers and other areas of construction consultancy including pool fencing certificates. Please see attached logos to incorporate to also match colour schemes with. Thanks!

Target Market(s)

Prospective buyers and home owners

Industry/Entity Type

Small Business

Requirements
Must have
• Promote the main services from the home page. Being able to select the type of service/certificate required from the main page and be directed to a specific page that deals with only that service containing the relevant information for that item.
Nice to have
• Small emphasis on the location of our office and areas we service etc.

```html
<!DOCTYPE html>
<html lang="en">
<head>
<meta charset="utf-8">
<title>Brookvale Assessors – Building Inspections Sydney</title>
<link rel="stylesheet" href="https://fonts.googleapis.com/css2?family=Roboto+Slab:wght@400;700&family=Arimo:wght@400;700&display=swap">
<style>
:root{
  --navy:#243447;
  --navy-dark:#1d2a3a;
  --blue:#1f7fc0;
  --blue-bright:#2a8fd2;
  --paper:#ece9e0;
  --field:#59687a;
  --white:#ffffff;
  --text:#3a3a3a;
  --muted:#cfd6de;
}
*{box-sizing:border-box;margin:0;padding:0}
html,body{width:796px;height:1200px;overflow:hidden}
body{position:relative;background:var(--paper);font-family:"Arimo",Arial,sans-serif;color:var(--text)}
.abs{position:absolute}
.topbar-contact{right:228px;top:21px;font-size:8.5px;font-weight:700;color:#111;white-space:nowrap;line-height:14px}
.topbar-contact .today{color:var(--blue)}
.topbar-contact .phone{color:var(--blue);font-size:12.5px;margin-left:2px}
.btn-book{left:575px;top:18px;width:130px;height:20px;background:var(--blue);color:var(--white);font-family:"Roboto Slab",serif;font-weight:700;font-size:10px;display:flex;align-items:center;justify-content:center;border-radius:3px;letter-spacing:.3px}
.navband{left:0;top:51px;width:796px;height:31px;background:var(--navy);border-top:1px dashed #6d7c8c;border-bottom:1px dashed #6d7c8c;z-index:1}
.brand{left:86px;top:20px;width:157px;height:70px;background:var(--white);box-shadow:0 2px 4px rgba(0,0,0,.35);display:flex;align-items:center;justify-content:center;gap:7px;z-index:2}
.brand-mark{width:16px;height:16px;background:var(--navy);flex:none}
.brand-name{font-family:"Arimo",sans-serif;font-weight:700;font-size:16px;color:var(--navy);line-height:1.05}
.nav{left:278px;top:51px;height:31px;display:flex;align-items:center;gap:0;font-size:10px;font-weight:700;color:var(--white);z-index:2}
.nav-home{width:20px;height:20px;border-radius:50%;background:var(--blue-bright);display:flex;align-items:center;justify-content:center;margin-right:33px}
.nav a{color:var(--white);text-decoration:none;margin-right:32px}
.hero{left:86px;top:103px;width:622px;height:199px;box-shadow:0 3px 6px rgba(0,0,0,.3);overflow:hidden}
.hero-photo{left:260px;top:0;width:362px;height:199px;background:linear-gradient(180deg,#c9ccc9 0%,#9eaab6 40%,#6f9a45 75%,#5b8a35 100%)}
.hero-title{left:14px;top:26px;width:200px;font-family:"Roboto Slab",serif;font-weight:700;font-size:16px;line-height:23px;color:var(--white)}
.dots{left:13px;top:182px;display:flex;gap:3px}
.dots span{width:6px;height:6px;background:#cfd6de}
.dots span:first-child{background:var(--navy)}
.cta{left:86px;top:318px;width:624px;height:44px;background:var(--blue);border-radius:6px}
.cta h2{left:10px;top:7px;font-size:13.5px;font-weight:700;color:var(--white)}
.cta p{left:11px;top:26px;font-size:8px;color:var(--white)}
.cta-btn{left:443px;top:7px;width:168px;height:31px;background:var(--navy);border-radius:4px;display:flex;align-items:center;color:var(--white);font-weight:700;font-size:15px}
.cta-btn .arrow{width:32px;height:31px;border-right:1px solid #4b5a6a;display:flex;align-items:center;justify-content:center;margin-right:8px}
.welcome{left:92px;top:375px;width:618px;height:114px;background:var(--white)}
.welcome h1{left:4px;top:8px;font-family:"Roboto Slab",serif;font-weight:400;font-size:15px;color:var(--navy)}
.welcome h1 b{font-family:"Arimo",sans-serif;font-size:20px;color:var(--navy)}
.welcome h1 span{color:var(--blue);font-family:"Arimo",sans-serif;font-size:15px;font-weight:700}
.rule{height:0;border-top:1px dashed #b9c0c8}
.welcome .rule{left:4px;top:36px;width:606px}
.welcome p{left:4px;top:44px;width:606px;font-size:8.4px;line-height:14px;color:#444}
.welcome p b{color:var(--navy)}
.services{left:92px;top:489px;width:618px;height:330px;background:var(--navy)}
.services h3,.booking h3{font-family:"Roboto Slab",serif;font-weight:400;font-size:14px;color:var(--white)}
.services h3{left:6px;top:10px}
.services .rule{left:6px;top:31px;width:316px;border-color:#5b6b7c}
.services .intro{left:6px;top:43px;width:326px;font-size:8.3px;line-height:14px;color:var(--white)}
.service-list{left:14px;top:116px;list-style:none}
.service-list li{display:flex;align-items:center;height:36px;font-family:"Roboto Slab",serif;font-size:10px;color:var(--white)}
.service-list li svg{width:36px;margin-right:16px}
.btn-more{left:252px;top:286px;width:78px;height:25px;background:var(--blue);color:var(--white);font-size:11.5px;display:flex;align-items:center;justify-content:center}
.booking{left:463px;top:499px;width:228px}
.booking .rule{left:0;top:21px;width:240px;border-color:#5b6b7c}
.booking h3{left:0;top:0}
.field{left:0;width:227px;height:18px;background:var(--field);color:var(--white);font-size:7.8px;padding:5px 10px;border-radius:1px}
.field.comments{height:52px;padding-top:4px;border-radius:3px}
.btn-submit{left:1px;top:276px;width:58px;height:25px;background:var(--blue);color:var(--white);font-size:11.5px;display:flex;align-items:center;justify-content:center}
.reviews-title{left:94px;top:843px;font-family:"Roboto Slab",serif;font-weight:700;font-size:13.5px;color:var(--navy)}
.review{top:875px;width:190px;font-size:8.5px;line-height:13.5px;font-style:italic;color:#555}
.review .q{position:absolute;left:-22px;top:-4px;font-family:"Roboto Slab",serif;font-size:24px;color:#b8bcc0;font-style:normal}
.review .qc{font-family:"Roboto Slab",serif;font-size:20px;color:#b8bcc0;font-style:normal;line-height:0;vertical-align:-9px;margin-left:4px}
.review .who{display:block;margin-top:8px;font-style:normal;color:#333}
.divider{top:878px;width:1px;height:78px;background:#d3d0c6}
.footer{left:0;top:987px;width:796px;height:165px;background:var(--navy)}
.footer h4{font-size:10px;font-weight:700;color:var(--white);padding-bottom:3px;border-bottom:1px dashed #6d7c8c;display:inline-block}
.quick{left:94px;top:12px}
.quick ul{list-style:none;margin-top:6px}
.quick li{font-size:8.8px;color:var(--white);height:17.5px}
.mapcol{left:218px;top:12px}
.map{margin-top:6px;width:170px;height:90px;border-radius:6px;background:linear-gradient(135deg,#e9e6df,#d8d4cb)}
.contact{left:424px;top:12px}
.contact dl{margin-top:8px;display:grid;grid-template-columns:20px 1fr;row-gap:10px;font-size:8.6px;color:var(--white);line-height:13px}
.contact dt{font-weight:700;font-size:10px}
.footer-brand{left:603px;top:100px;font-weight:700;font-size:13px;color:#4b5b6c;display:flex;align-items:center;gap:6px}
.footer-brand i{width:14px;height:14px;background:#4b5b6c;display:block}
.bottom{left:0;top:1152px;width:796px;height:28px;background:var(--blue)}
.bottom p{left:94px;top:9px;font-size:8px;color:#1d2a3a}
.social{left:627px;top:4px;display:flex;gap:7px}
.social span{width:19px;height:19px;border-radius:50%;background:#5aa8e0;display:block}
.social span:nth-child(2){background:#3f63a8}
.social span:nth-child(3){background:#1d6fa8}
</style>
</head>
<body>

<div class="abs navband"></div>
<div class="abs brand"><span class="brand-mark"></span><span class="brand-name">Brookvale<br>Assessors</span></div>
<div class="abs topbar-contact">Contact us <span class="today">Today :</span> <span class="phone">123-456-7890</span></div>
<div class="abs btn-book">BOOK AN INSPECTION</div>

<nav class="abs nav">
  <span class="nav-home"><svg width="12" height="11" viewBox="0 0 12 11"><path d="M6 0L0 5h2v6h3V7h2v4h3V5h2z" fill="#fff"/></svg></span>
  <a href="#">About Us</a><a href="#">Services</a><a href="#">Our Consultants</a><a href="#">Pricing</a><a href="#">Contact Us</a>
</nav>

<section class="abs hero">
  <div class="abs hero-photo" role="img" aria-label="Photo of a smiling family sitting on the lawn in front of their house"></div>
  <svg class="abs" style="left:0;top:0" width="622" height="199" viewBox="0 0 622 199">
    <path d="M0 0H300C280 20 250 80 230 199H0Z" fill="#1f7fc0"/>
    <path d="M300 0C280 20 250 80 230 199L205 199C220 170 225 120 300 0Z" fill="#243447"/>
  </svg>
  <h2 class="abs hero-title">We offer pre-purchase building inspections &amp; combined pre-purchase building &amp; pest inspections</h2>
  <div class="abs dots"><span></span><span></span><span></span><span></span></div>
</section>

<section class="abs cta">
  <h2 class="abs">Lorem ipsum dolor sit amet consectetuer adipiscing adipiscin</h2>
  <p class="abs">consectetuer adipiscing elit, sed diam nonummy nibh euismod tincidunt</p>
  <div class="abs cta-btn"><span class="arrow"><svg width="16" height="16" viewBox="0 0 16 16"><path d="M2 5h6V1l7 7-7 7v-4H2z" fill="#2a8fd2"/></svg></span>Get Started Now!</div>
</section>

<section class="abs welcome">
  <h1 class="abs">Welcome to <b>Brookvale</b> <span>ASSESSORS</span></h1>
  <div class="abs rule"></div>
  <p class="abs">Lorem ipsum dolor sit amet consectetur adipisicing elitsed do eiusmod tempor incididunt ut labore dolo magna aliqua. Ut enim ad minim veniam, quis nostrud exercitation ullamco laboris nisi ut aliquip ex comm consequat. Duis aute irure dolor in reprehenderit in voluptate velit esse cillum dolore eu fugiat nulla pariatur. Duis aute irure dolor in reprehenderit in voluptate velit esse cillum dolore eu fugiat nulla pariatur. Excepteur si occaecat cupidatat non proidentin reprehenderit in voluptate velit esse cillum dolore eu fugiat nulla pariatur<b>...Read More</b> i</p>
</section>

<section class="abs services">
  <h3 class="abs">Our Services</h3>
  <div class="abs rule"></div>
  <p class="abs intro">Lorem ipsum dolor sit amet consectetur adipisicing elitsed do eiusmod tempor incididunt ut labore dolo magna aliqua. Ut enim ad minim veniam, quis nostrud dfre rreexercitation ullamco laboris nisi ut aliquip ex comm consequat. Duis aute irure dolor in reprehenderit in voluptate velit esse cillum dolore eu fugiat nulla.</p>
  <ul class="abs service-list">
    <li><svg height="28" viewBox="0 0 36 28"><path d="M6 12L16 4l10 8v12H6z" fill="none" stroke="#fff" stroke-width="2"/><path d="M11 16l5 5 14-16" fill="none" stroke="#fff" stroke-width="3"/></svg>Complete Pre-purchase Building Inspection</li>
    <li><svg height="28" viewBox="0 0 36 28"><rect x="8" y="4" width="22" height="20" fill="none" stroke="#fff" stroke-width="2"/><path d="M6 6l20 18" stroke="#fff" stroke-width="3"/></svg>Structural Plus Pre-purchase Building Inspection</li>
    <li><svg height="28" viewBox="0 0 36 28"><path d="M18 2L4 14h4v12h20V14h4z" fill="#fff"/><rect x="15" y="17" width="6" height="9" fill="#243447"/></svg>Combined Building &amp; Pest Inspection</li>
    <li><svg height="28" viewBox="0 0 36 28"><path d="M2 18l16 8 16-8-16-6z" fill="none" stroke="#fff" stroke-width="2"/><path d="M12 16l5 4 12-16" fill="none" stroke="#fff" stroke-width="3"/></svg>Pool Safety Inspection</li>
    <li><svg height="28" viewBox="0 0 36 28"><path d="M18 2L4 14h4v12h20V14h4z" fill="none" stroke="#fff" stroke-width="2.5"/><circle cx="18" cy="18" r="3" fill="#fff"/></svg>Defects Liability Period Inspection</li>
  </ul>
  <div class="abs btn-more">READ MORE</div>
</section>

<form class="abs booking">
  <h3 class="abs">Booking Request</h3>
  <div class="abs rule"></div>
  <div class="abs field" style="top:35px">Your Name*</div>
  <div class="abs field" style="top:58px">Email Address*</div>
  <div class="abs field" style="top:81px">Phone Number*</div>
  <div class="abs field" style="top:104px">What kind of service is it regarding?</div>
  <div class="abs field" style="top:127px">Address of property to be inspected?</div>
  <div class="abs field" style="top:149px">Property Agent's name &amp; contact details?</div>
  <div class="abs field" style="top:172px">Tenant / Owner Contact Details?</div>
  <div class="abs field" style="top:195px">Inspection required by (date)?</div>
  <div class="abs field comments" style="top:219px">Comments</div>
  <div class="abs btn-submit">SUBMIT</div>
</form>

<h3 class="abs reviews-title">Words from Some of our Happy Customers</h3>
<blockquote class="abs review" style="left:118px"><span class="q">“</span>Lorem ipsum dolor sit amet consectetur adipisicing elitsed do eiusmod tempor incididunt ut labore dolo magna aliqua. Ut enim ad mini.<span class="qc">”</span><span class="who">Morgan Hale -Lorem Ispum</span></blockquote>
<div class="abs divider" style="left:295px"></div>
<blockquote class="abs review" style="left:321px"><span class="q">“</span>Lorem ipsum dolor sit amet consectetur adipisicing elitsed do eiusmod tempor incididunt ut labore dolo magna aliqua. Ut enim ad mini.<span class="qc">”</span><span class="who">Morgan Hale -Lorem Ispum</span></blockquote>
<div class="abs divider" style="left:499px"></div>
<blockquote class="abs review" style="left:534px;top:878px"><span class="q">“</span>Lorem ipsum dolor sit amet consectetur adipisicing elitsed.<span class="qc">”</span><span class="who">Morgan Hale -Lorem Ispum</span></blockquote>

<footer class="abs footer">
  <div class="abs quick"><h4>Quick Links</h4>
    <ul><li>HOME</li><li>ABOUT US</li><li>SERVICES</li><li>OUR CONSULTANTS</li><li>PRICING</li><li>CONTACT US</li></ul>
  </div>
  <div class="abs mapcol"><h4>Location Map</h4>
    <div class="map" role="img" aria-label="Street map showing the office location"></div>
  </div>
  <div class="abs contact"><h4>Contact Information</h4>
    <dl><dt>A:</dt><dd>Street Name, City Name<br>State Zipcode</dd><dt>P:</dt><dd>123 456 7890</dd><dt>TF:</dt><dd>1800 456 7890</dd><dt>E:</dt><dd>inquiry@brookvaleassessors.com</dd></dl>
  </div>
  <div class="abs footer-brand"><i></i>Brookvale<br>Assessors</div>
</footer>

<div class="abs bottom">
  <p class="abs">Copyright ©2014, BrookvaleAssessors  All Rights Reserved</p>
  <div class="abs social"><span></span><span></span><span></span></div>
</div>

</body>
</html>
```